Swerve (nightclub flyer)

Nightclub flyer, guaranteed project. Text below (and please use logos, large):

SWERVE PRESENTS:

KORVEN (LOGO) B2B MARTY DELANO (LOGO)

+TOBBI RASK (smaller text)

10/26/17

2284 ELM LANE SACRAMENTO CA
21+ 10PM-2AM

HOUSE/TECHNO

A VELVET ORCHID ENTERTAINMENT (LOGO) PRODUCTION

Target Market(s)

House/Electronic Music Lovers

Industry/Entity Type

Night Club

Font styles to use
Sans Serif

Colors

Designer to choose colors to be used in the design.

Requirements
Must have
• Large logos for the dj names, or large block letter dj names (logos not necessary if it looks better without. But KORVEN b2b MARTY DELANO large and TOBBI RASK smaller on separate line
Nice to have
• Can include a classy female model but nothing cheesy or too sexy

```html
<!DOCTYPE html>
<html lang="en">
<head>
<meta charset="utf-8">
<title>Swerve Presents Korven</title>
<link rel="stylesheet" href="https://fonts.googleapis.com/css2?family=Bungee&family=Oswald:wght@400;700&display=swap">
<style>
  :root {
    --night-purple: #4a2f5c;
    --deep-violet: #3a2450;
    --slate: #566484;
    --navy-ink: #2b3690;
    --ice: #e2f6f7;
    --white: #ffffff;
  }
  * { margin: 0; padding: 0; box-sizing: border-box; }
  html, body { width: 927px; height: 1200px; overflow: hidden; background: var(--deep-violet); }
  .flyer { position: relative; width: 927px; height: 1200px; overflow: hidden; }
  .club-photo {
    position: absolute; inset: 0;
    background:
      radial-gradient(ellipse 320px 260px at 260px 80px, rgba(255,255,255,0.55), transparent 70%),
      radial-gradient(ellipse 340px 300px at 720px 400px, rgba(70,220,240,0.75), transparent 70%),
      radial-gradient(ellipse 260px 200px at 40px 330px, rgba(230,40,150,0.6), transparent 70%),
      radial-gradient(ellipse 300px 260px at 820px 80px, rgba(240,150,90,0.45), transparent 70%),
      radial-gradient(ellipse 280px 360px at 330px 560px, rgba(230,190,200,0.45), transparent 70%),
      linear-gradient(160deg, #7b63b8 0%, #4a67b5 35%, #2a88b8 60%, #2e4f86 100%);
  }
  .color-planes { position: absolute; inset: 0; width: 927px; height: 1200px; }
  .headline {
    position: absolute; top: 36px; left: 0; width: 927px; text-align: center;
    font-family: "Bungee", sans-serif; font-size: 70px; line-height: 1; letter-spacing: -1px;
    background: linear-gradient(90deg, #1f3fa8 0%, #4a62c8 35%, #a24fc0 65%, #d84aa6 100%);
    -webkit-background-clip: text; background-clip: text; color: transparent;
  }
  .dj-mark { position: absolute; left: 120px; top: 128px; width: 230px; text-align: center; }
  .dj-mark__dot {
    width: 84px; height: 84px; margin: 0 auto; border-radius: 50%;
    background: #151a22; border: 3px solid var(--white);
  }
  .dj-mark__name {
    margin-top: 8px; font-family: "Oswald", sans-serif; font-weight: 700;
    font-size: 32px; line-height: 1; letter-spacing: 1px; color: var(--white);
  }
  .b2b {
    position: absolute; left: 362px; top: 192px;
    font-family: "Oswald", sans-serif; font-weight: 700; font-size: 38px; line-height: 1;
    color: var(--ice);
  }
  .headliner {
    position: absolute; left: 452px; top: 172px;
    font-family: "Bungee", sans-serif; font-size: 68px; line-height: 1; letter-spacing: 2px;
    color: var(--navy-ink);
  }
  .support {
    position: absolute; left: 262px; top: 302px;
    font-family: "Oswald", sans-serif; font-weight: 700; font-size: 60px; line-height: 1;
    color: var(--ice);
  }
  .details {
    position: absolute; left: 0; top: 800px; width: 896px; text-align: center;
    font-family: "Oswald", sans-serif; font-weight: 700; color: var(--white);
    letter-spacing: 5px;
  }
  .details__date { font-size: 46px; line-height: 56px; margin-bottom: 20px; }
  .details__line { font-size: 42px; line-height: 52px; }
  .production {
    position: absolute; left: 0; top: 1158px; width: 896px; text-align: center;
    font-family: "Oswald", sans-serif; font-weight: 400; font-size: 18px; line-height: 1;
    letter-spacing: 3px; color: var(--white);
  }
</style>
</head>
<body>
<main class="flyer">
  <div class="club-photo" role="img" aria-label="Photo of smiling couple and a woman dancing under colorful nightclub lasers"></div>

  <svg class="color-planes" viewBox="0 0 1159 1500" preserveAspectRatio="none" aria-hidden="true">
    <polygon points="0,815 360,910 870,1040 1159,1100 1159,1500 0,1500" fill="var(--night-purple)" opacity="0.95"/>
    <polygon points="860,1040 1140,1110 1159,1500" fill="var(--slate)" opacity="0.9"/>
    <polygon points="0,1300 0,1500 1159,1500 1159,1420" fill="var(--deep-violet)" opacity="0.5"/>
  </svg>

  <h1 class="headline">SWERVE PRESENTS</h1>

  <div class="dj-mark">
    <div class="dj-mark__dot"></div>
    <div class="dj-mark__name">MARTY DELANO</div>
  </div>

  <span class="b2b">B2B</span>

  <h2 class="headliner">KORVEN</h2>

  <p class="support">+TOBBI RASK</p>

  <section class="details">
    <p class="details__date">10/26/17</p>
    <p class="details__line">2284 ELM LANE</p>
    <p class="details__line">SACRAMENTO CA</p>
    <p class="details__line">21+</p>
    <p class="details__line">10PM-2AM</p>
    <p class="details__line">HOUSE/TECHNO</p>
  </section>

  <p class="production">A VELVET ORCHID ENTERTAINMENT PRODUCTION</p>
</main>
</body>
</html>
```